International sports company needs packaging design for color box

We need this box for our yoga mats which we will sell online. This mat is very high quality and 100% environmentally friendly. The yoga mat comes in a stylish yoga bag that will be in the box.

Yoga enthusiasts, athletes, gymnasts, actually all people who do sporting activities and value environmental friendliness will be the contact group

The logo should be visible in any case. The creator is free to choose whether to use only the complete logo or the complete logo with the emblem. In terms of style, it should be reminiscent of a packaging box from Corvane's Zentrix. Be as timeless, modern and elegant as possible. If an environmentally friendly detail can be added, this would certainly be a plus. Color should be black / white / gray.

Target Market(s)

Germany

Requirements
Must have
• Size for the color box should be 13x13x61.5 cm.

```html
<!DOCTYPE html>
<html lang="en">
<head>
<meta charset="utf-8">
<title>Yoga Mat Box – Flat Net</title>
<link href="https://fonts.googleapis.com/css2?family=Archivo:ital,wght@0,500;1,400&display=swap" rel="stylesheet">
<style>
  :root {
    --page: #ffffff;
    --panel: #ffffff;
    --fold: #8c8c8c;
    --type-grey: #8a8a8a;
    --brand-black: #111111;
    --mat-light: #ececec;
    --mat-mid: #d6d6d6;
    --mat-dark: #a9a9a9;
    --icon-grey: #8f8f8f;
  }
  html, body {
    margin: 0;
    padding: 0;
    width: 971px;
    height: 1200px;
    overflow: hidden;
    background: var(--page);
  }
  .canvas {
    position: relative;
    width: 971px;
    height: 1200px;
  }
  .box-net {
    position: absolute;
    left: 25px;
    top: 215px;
    width: 920px;
    height: 770px;
    background: var(--panel);
  }
  .box-net__art {
    position: absolute;
    inset: 0;
    width: 920px;
    height: 770px;
  }
  .product-title {
    position: absolute;
    margin: 0;
    font-family: "Archivo", sans-serif;
    font-style: italic;
    font-weight: 400;
    color: var(--type-grey);
    line-height: 1;
    letter-spacing: 0.01em;
    white-space: nowrap;
  }
  .product-title--small { left: 43px; top: 528px; font-size: 23px; }
  .product-sub--small { left: 70px; top: 554px; font-size: 11px; }
  .product-title--large { left: 43px; top: 672px; font-size: 36px; }
  .product-sub--large { left: 89px; top: 713px; font-size: 19px; }
  .brand {
    position: absolute;
    display: flex;
    align-items: center;
    gap: 8px;
    font-family: "Archivo", sans-serif;
    font-weight: 500;
    color: var(--brand-black);
    letter-spacing: 0.12em;
    white-space: nowrap;
    transform: translate(-50%, -50%);
  }
  .brand__square {
    background: var(--brand-black);
  }
  .brand--side { left: 470px; top: 493px; font-size: 26px; }
  .brand--side .brand__square { width: 14px; height: 14px; }
  .brand--front { left: 470px; top: 702px; font-size: 24px; }
  .brand--front .brand__square { width: 13px; height: 13px; }
  .eco-icons {
    position: absolute;
    left: 812px;
    top: 694px;
    display: flex;
    gap: 8px;
  }
</style>
</head>
<body>
<main class="canvas">
  <section class="box-net" aria-label="Yoga mat box, flat net with four panels">
    <svg class="box-net__art" viewBox="0 0 1111 930" preserveAspectRatio="none">
      <defs>
        <linearGradient id="mat-tone" x1="0" y1="0" x2="1" y2="1">
          <stop offset="0" stop-color="#d6d6d6"/>
          <stop offset="0.55" stop-color="#ececec"/>
          <stop offset="0.78" stop-color="#a9a9a9"/>
          <stop offset="0.88" stop-color="#ececec"/>
          <stop offset="1" stop-color="#d6d6d6"/>
        </linearGradient>
      </defs>
      <polygon class="mat-photo" role="img" aria-label="Photograph of a textured grey yoga mat, rolled up at the lower right"
               points="712,0 1111,420 1111,930 479,930 117,495" fill="url(#mat-tone)"/>
      <g class="fold-lines" stroke="#8c8c8c" stroke-width="1" fill="none">
        <rect x="0.5" y="0.5" width="1110" height="929"/>
        <line x1="0" y1="237" x2="1111" y2="237"/>
        <line x1="0" y1="470" x2="1111" y2="470"/>
        <line x1="0" y1="705" x2="1111" y2="705"/>
      </g>
    </svg>

    <h2 class="product-title product-title--small">YOGA MAT</h2>
    <p class="product-title product-sub--small">WITH BAG</p>
    <div class="brand brand--side"><span class="brand__square"></span>VELQORA</div>

    <h1 class="product-title product-title--large">YOGA MAT</h1>
    <p class="product-title product-sub--large">WITH BAG</p>
    <div class="brand brand--front"><span class="brand__square"></span>VELQORA</div>

    <div class="eco-icons">
      <svg width="42" height="42" viewBox="0 0 42 42" role="img" aria-label="Eco-friendly mat icon">
        <g fill="none" stroke="#8f8f8f" stroke-width="1.6">
          <rect x="9" y="9" width="24" height="24" transform="rotate(45 21 21)"/>
          <path d="M16 26 C16 18 22 14 27 14 C27 21 23 26 16 26 Z"/>
          <path d="M16 26 L23 19"/>
        </g>
      </svg>
      <svg width="42" height="42" viewBox="0 0 42 42" role="img" aria-label="Recycling icon">
        <g fill="none" stroke="#8f8f8f" stroke-width="2" stroke-linejoin="round" stroke-linecap="round">
          <path d="M23 9 L31 23"/>
          <path d="M27 22 L31 23 L32 19"/>
          <path d="M31 33 L13 33"/>
          <path d="M16 30 L13 33 L16 36"/>
          <path d="M9 30 L17 15"/>
          <path d="M13 16 L17 15 L18 19"/>
        </g>
      </svg>
    </div>
  </section>
</main>
</body>
</html>
```